Business Card Re-Design...or logo does not look sharp

Hello

We are a start-up and just need someone to help us.

Our colors are: Marlowe Hush pink (yeah I know) and charcoal for the lettering.

I am attaching our logo which needs cleaning up.

We want the JUST the lady ironing on the table (pink) in front, and the background in charcoal. All the business info can be on the back.

Dims on card are 2 x 2''

Also, if you have better ideas....please let us know!

Thanks

Gregory

La Comadre Vapor
4827 Quellbrook Dr Suite B2
El Paso TX 79936
915-555-0148

```html
<!DOCTYPE html>
<html lang="en">
<head>
<meta charset="utf-8">
<title>La Comadre Vapor — Business Card</title>
<link rel="stylesheet" href="https://fonts.googleapis.com/css2?family=Dancing+Script:wght@500&family=Delius&display=swap">
<style>
  :root {
    --backdrop: #ece9e6;
    --charcoal: #232122;
    --charcoal-damask: #2d2a2b;
    --blush: #e6cfcb;
    --blush-damask: #dcbfbb;
    --logo-pink: #f2c9c4;
    --ink: #1f1c1d;
    --band-text: #f3e6e3;
    --card-shadow: 0 10px 28px rgba(0, 0, 0, 0.22);
  }

  * { box-sizing: border-box; margin: 0; padding: 0; }

  html, body {
    width: 1200px;
    height: 865px;
    overflow: hidden;
    background: var(--backdrop);
  }

  .card-sheet {
    width: 1200px;
    height: 865px;
    display: flex;
    align-items: center;
    justify-content: center;
    gap: 60px;
  }

  .card {
    position: relative;
    width: 480px;
    height: 480px;
    border-radius: 4px;
    overflow: hidden;
    box-shadow: var(--card-shadow);
    flex: none;
  }

  .card-texture {
    position: absolute;
    inset: 0;
  }

  /* Front */
  .card-front { background: var(--charcoal); }
  .card-front .card-texture {
    background: radial-gradient(ellipse at center, var(--charcoal-damask) 0%, var(--charcoal) 75%);
  }

  .brand-mark {
    position: absolute;
    left: 50%;
    top: 50%;
    width: 150px;
    height: 150px;
    margin: -75px 0 0 -75px;
    border-radius: 50%;
    background: var(--logo-pink);
  }

  /* Back */
  .card-back { background: var(--blush); }
  .card-back .card-texture {
    background: linear-gradient(160deg, var(--blush) 0%, var(--blush-damask) 100%);
  }

  .business-name {
    position: absolute;
    left: 30px;
    top: 44px;
    font-family: "Dancing Script", cursive;
    font-weight: 500;
    font-size: 54px;
    line-height: 1;
    color: var(--ink);
    white-space: nowrap;
  }

  .address-band {
    position: absolute;
    left: 0;
    right: 0;
    top: 122px;
    height: 38px;
    background: var(--charcoal);
    display: flex;
    align-items: center;
    justify-content: center;
    font-family: "Delius", sans-serif;
    font-size: 15px;
    color: var(--band-text);
    white-space: nowrap;
  }

  .address-part { padding: 0 10px; }
  .address-part + .address-part { border-left: 1.5px solid var(--band-text); }

  .phone-line {
    position: absolute;
    right: 36px;
    bottom: 44px;
    display: flex;
    align-items: center;
    gap: 8px;
    font-family: "Delius", sans-serif;
    font-size: 28px;
    color: var(--ink);
    letter-spacing: 1px;
    white-space: nowrap;
  }

  .phone-icon { width: 34px; height: 29px; }
</style>
</head>
<body>
  <main class="card-sheet">
    <section class="card card-front" aria-label="Card front">
      <div class="card-texture" role="img" aria-label="Charcoal damask pattern background"></div>
      <div class="brand-mark" role="img" aria-label="Brand mark area"></div>
    </section>

    <section class="card card-back" aria-label="Card back">
      <div class="card-texture" role="img" aria-label="Soft pink damask pattern background"></div>
      <h1 class="business-name">La Comadre Vapor</h1>
      <div class="address-band">
        <span class="address-part">4827 Quellbrook</span>
        <span class="address-part">Dr Suite B2</span>
        <span class="address-part">El Paso TX 79936</span>
      </div>
      <div class="phone-line">
        <svg class="phone-icon" viewBox="0 0 40 34" aria-hidden="true">
          <path d="M3 11 C3 4 37 4 37 11 L37 14 L29 14 L29 10 L11 10 L11 14 L3 14 Z" fill="var(--ink)"/>
          <path d="M9 15 L31 15 L35 31 L5 31 Z" fill="var(--ink)"/>
          <circle cx="20" cy="23" r="5" fill="var(--blush)"/>
          <circle cx="20" cy="23" r="2" fill="var(--ink)"/>
        </svg>
        <span class="phone-number">915-555-0148</span>
      </div>
    </section>
  </main>
</body>
</html>
```